Graphical design for food product in 1 Liter carton

We need this design not for a real product but as a showcase for a new service.

This special situation makes it really simple for you to participate because you only have to care about how the visual impression of your design is.

Furthermore it gives you the opportunity to get an extra winning chance if you choose to also participate in the open competition at our website - where you can enter the same design as you enter here at ArtQuarry.

Here is the requirements:

1. You must apply your design to our attatched template

2. Make a design for a food product of your own choice, which is to be sold from retail stores in a rectangular 1 L carton – based on our template.

3. You are only allowed to use brand names and/or logos that you have the rights to use for this competition, so please make completely fictive brand names and logos.

4. Your design is evaluated on the visual impression only, which means that your text on the design can be in any language and doesn’t have to relate to the design.

5. The criteria for the evaluation of your design is your creativity, the graphical quality and how well the product will display it self in the stores.

If you also want to participate in the open competition on our website - where you can win an Zelbo Slate, and will get your design skills exposed to brand owners and packaging manufacturers all over the world, then please visit plovimark.example/packaging-design-competition/

Attatched is:

A. Empty design template you must apply your design to. Remove the layer with our template when you return your send in your design.

B. Example of design applied to the template.

C. Example of the applied example design after it has been converted to 3D with our online 3D engine at PloviMark.example.

The winning design will be converted to 3D and will be used as a showcase on our website - all designers can enter their design to our open competition at PloviMark.example.

```html
<!DOCTYPE html>
<html lang="en">
<head>
<meta charset="utf-8">
<title>Fernly Vegetable Broth – carton layout</title>
<link rel="stylesheet" href="https://fonts.googleapis.com/css2?family=Arimo:wght@400;700&display=swap">
<style>
  :root {
    --page-bg: #1c1c1c;
    --carton-top: #ffffff;
    --carton-mid: #fbe58c;
    --carton-low: #f6c93a;
    --carton-base: #eea81c;
    --brand-ink: #2a2320;
    --title-red: #8e1b1f;
    --tag-red: #c0262b;
    --claim-green: #1f6e1f;
    --fold-line: #b9b9b9;
    --flap: #f2f2f2;
    --text-dark: #222222;
  }
  * { margin: 0; padding: 0; box-sizing: border-box; }
  html, body { width: 1200px; height: 1076px; overflow: hidden; }
  body {
    background: var(--page-bg);
    font-family: "Arimo", Arial, sans-serif;
    color: var(--text-dark);
    position: relative;
  }
  .dieline {
    position: absolute;
    left: 70px;
    top: 70px;
    width: 1060px;
    height: 936px;
  }
  .flap-row {
    position: absolute;
    left: 0;
    height: 60px;
    display: flex;
  }
  .flap-row.top { top: 0; }
  .flap-row.bottom { bottom: 0; }
  .flap {
    background: var(--flap);
    border: 1px solid var(--fold-line);
    height: 100%;
  }
  .panels {
    position: absolute;
    top: 60px;
    left: 0;
    height: 816px;
    display: flex;
  }
  .panel {
    position: relative;
    height: 100%;
    border-right: 1px dashed var(--fold-line);
    background: linear-gradient(180deg, var(--carton-top) 0%, var(--carton-top) 22%, var(--carton-mid) 45%, var(--carton-low) 75%, var(--carton-base) 100%);
    overflow: hidden;
  }
  .w-side { width: 210px; }
  .w-face { width: 310px; }
  .w-glue { width: 20px; background: var(--flap); border: 1px solid var(--fold-line); }

  /* brand + title */
  .brand-name {
    font-weight: 700;
    color: var(--brand-ink);
    font-size: 62px;
    letter-spacing: 1px;
    text-align: center;
    line-height: 1;
  }
  .tagline {
    color: var(--tag-red);
    font-size: 12px;
    text-align: right;
    margin-top: 6px;
  }
  .product-title {
    color: var(--title-red);
    font-size: 40px;
    font-weight: 400;
    line-height: 1.05;
    text-align: right;
    margin-top: 8px;
  }
  .face-head { position: absolute; top: 70px; left: 26px; right: 22px; }

  .serving-claim {
    position: absolute;
    top: 268px;
    right: 22px;
    width: 170px;
    text-align: right;
    color: var(--claim-green);
    font-size: 13px;
    line-height: 1.35;
  }

  .veg-art {
    position: absolute;
    left: 0; right: 0; top: 330px; bottom: 0;
    background:
      radial-gradient(circle at 22% 12%, rgba(250,200,60,0.9) 0 14%, transparent 15%),
      radial-gradient(circle at 78% 28%, rgba(226,80,40,0.85) 0 13%, transparent 14%),
      radial-gradient(circle at 40% 75%, rgba(255,255,235,0.85) 0 11%, transparent 12%),
      linear-gradient(160deg, rgba(120,170,40,0.35), rgba(240,130,30,0.45));
  }
  .cert-stack {
    position: absolute; left: 18px; bottom: 90px;
    display: flex; flex-direction: column; gap: 10px;
  }
  .cert-mark {
    width: 30px; height: 30px; border-radius: 50%;
    border: 2px solid var(--text-dark);
    background: var(--carton-mid);
  }
  .cert-mark.leaf { border-color: var(--claim-green); }
  .volume {
    position: absolute; right: 20px; bottom: 38px;
    text-align: right; font-size: 13px; line-height: 1.4;
  }

  /* side panels */
  .side-body { position: absolute; top: 40px; left: 16px; right: 16px; font-size: 10px; line-height: 1.45; }
  .nutrition {
    border: 2px solid var(--text-dark);
    background: #ffffff;
    padding: 6px 7px;
    font-size: 10px;
  }
  .nutrition h3 { font-size: 17px; font-weight: 700; border-bottom: 5px solid var(--text-dark); padding-bottom: 2px; margin-bottom: 3px; }
  .nutrition .row { display: flex; justify-content: space-between; border-bottom: 1px solid var(--text-dark); padding: 2px 0; }
  .ingredients { margin-top: 10px; font-size: 9.5px; }
  .contact { position: absolute; left: 16px; right: 16px; bottom: 40px; text-align: center; }
  .contact .brand-name { font-size: 40px; }
  .contact p { font-size: 11px; line-height: 1.4; margin-top: 6px; }
  .story { font-size: 11px; line-height: 1.55; }
</style>
</head>
<body>
  <main class="dieline">
    <div class="flap-row top">
      <div class="flap" style="width:210px"></div>
      <div class="flap" style="width:310px"></div>
      <div class="flap" style="width:210px"></div>
      <div class="flap" style="width:310px"></div>
    </div>

    <div class="panels">
      <section class="panel w-side info-side">
        <div class="side-body">
          <div class="nutrition">
            <h3>Nutrition Facts</h3>
            <div class="row"><span>Serving Size 1 cup (240ml)</span></div>
            <div class="row"><span>Servings about 4</span></div>
            <div class="row"><b>Calories 15</b></div>
            <div class="row"><span>Total Fat 0g</span></div>
            <div class="row"><span>Sodium 480mg</span></div>
            <div class="row"><span>Total Carb 3g</span></div>
            <div class="row"><span>Sugars 1g</span></div>
            <div class="row"><span>Protein 1g</span></div>
            <div class="row"><span>Vitamin A 60%</span></div>
          </div>
          <p class="ingredients"><b>INGREDIENTS:</b> Filtered water, kale, onion, carrot, tomato, celery, parsley, cauliflower, sea salt. <b>ALLERGENS:</b> Contains none.</p>
        </div>
        <div class="contact">
          <div class="brand-name">Fernly</div>
          <p>Questions or comments?<br>Consumer affairs<br>1180 Orchard Lane<br>Brookvale, ST 40210</p>
        </div>
      </section>

      <section class="panel w-face front-face">
        <div class="veg-art" role="img" aria-label="Painted onion, tomato, carrot, cauliflower and parsley illustration"></div>
        <div class="face-head">
          <div class="brand-name">Fernly</div>
          <p class="tagline">Eat Fernly. Natural is Delicious !</p>
          <h1 class="product-title">Vegetable<br>Broth</h1>
        </div>
        <p class="serving-claim">A full serving of kale<br>plus seven more vegetables</p>
        <div class="cert-stack">
          <span class="cert-mark leaf"></span>
          <span class="cert-mark"></span>
          <span class="cert-mark"></span>
          <span class="cert-mark"></span>
        </div>
        <p class="volume">32 Fl Oz (1 QT)<br>946 ml</p>
      </section>

      <section class="panel w-side story-side">
        <div class="side-body">
          <p class="story">Our broth is simmered slowly from kale, onion, carrot, tomato and fresh herbs for a clean, bright taste. Enjoy it warm in a mug, or use it as the base for soups, risotto and sauces. Shake well and refrigerate after opening. Use within ten days.</p>
        </div>
      </section>

      <section class="panel w-face back-face">
        <div class="veg-art" role="img" aria-label="Painted tomato, carrot, peas and parsley illustration"></div>
        <div class="face-head">
          <div class="brand-name">Fernly</div>
          <p class="tagline">Eat Fernly. Natural is Delicious !</p>
          <h1 class="product-title">Vegetable<br>Broth</h1>
        </div>
        <p class="serving-claim">A full serving of kale<br>plus seven more vegetables</p>
        <div class="cert-stack">
          <span class="cert-mark leaf"></span>
          <span class="cert-mark"></span>
        </div>
      </section>

      <div class="w-glue" aria-hidden="true"></div>
    </div>

    <div class="flap-row bottom">
      <div class="flap" style="width:210px"></div>
      <div class="flap" style="width:310px"></div>
      <div class="flap" style="width:210px"></div>
      <div class="flap" style="width:310px"></div>
    </div>
  </main>
</body>
</html>
```